Counsel Atelier

we need all the matirials for the office to speak with the internet site
www.cunatel.example

look stilish and modern yet very respecteble

our logo needs to be our logo and some times

just the letters " Cunatel " done nicely.

We need to send e mails with a design

Firm paper

and our gmail products to look nice when we use google docs

so we need a place for

lawers names and

the cunatel

and logo

and address

and some one to help us do it all

Target Market(s)

Big firms

Industry/Entity Type

Law Firm

Font styles to use
Serif

Requirements
Must have
• Rememrable
• Different yet respectable
• For multi languages
• LAW
• B
• LAWYERS
• BOUTIQUE
Nice to have
• Clean Design
• impressive
• i put on a new card i liked
• We should not put any decorations and beautiful logo
• it's against the law for lawyers
• I have a card that proves that we are smart and boutiques
• This card that I attached as an example
• Makes you little work, and certainly - apart from everyone
• Would love this design idea
• The numbers stated hiding it from top to bottom
• I put my real information integration profile
• The thing is that people should enlighten other options and other card
• This should be accessible designer fee changes
• Still very respectable and serious
• it needs to say among other creative stuff
• Counsel atelier CUNATEL
• TOMAS VELLINGRO
• 052-7164291
• 1@cunatel.example
• www.cunatel.example
• but any smart idea
Should not have
• We have a problam
• It turns out that the law of the Bar Association in
• Our country
• Do not allow to put the firm logo on business cards
• Or office paper
• the logo can only be letters and names
• So we should convey the idea of all sorts of areas along
• As we tried with our logo
• Through the letters themselves
• And their integration with each other

```html
<!DOCTYPE html>
<html lang="en">
<head>
<meta charset="utf-8">
<title>Cunatel — Business Card</title>
<link rel="stylesheet" href="https://fonts.googleapis.com/css2?family=Cinzel:wght@400;500&family=Source+Sans+3:wght@400;600&display=swap">
<style>
  :root {
    --backdrop: #9c9d9e;
    --card-paper: #ececee;
    --navy: #0b2a63;
    --ink: #4a4d52;
    --muted: #9a9ca0;
    --reverse-text: #e4e6ec;
    --url-text: #c4cad8;
  }
  * { margin: 0; padding: 0; box-sizing: border-box; }
  html, body {
    width: 1105px;
    height: 1200px;
    overflow: hidden;
    background: var(--backdrop);
  }
  .canvas {
    position: relative;
    width: 1105px;
    height: 1200px;
  }
  .card {
    position: absolute;
    left: 182px;
    width: 746px;
    height: 424px;
  }
  .card--front { top: 120px; background: var(--card-paper); }
  .card--back  { top: 637px; background: var(--navy); }

  .wordmark {
    font-family: "Cinzel", "Times New Roman", serif;
    font-weight: 500;
    line-height: 1;
  }
  .card--front .wordmark {
    position: absolute;
    left: 58px;
    top: 58px;
    font-size: 86px;
    color: var(--navy);
  }
  .contact {
    position: absolute;
    left: 60px;
    top: 222px;
    font-family: "Source Sans 3", "Helvetica Neue", Arial, sans-serif;
    font-size: 19px;
    line-height: 27px;
    color: var(--ink);
    list-style: none;
  }
  .contact__address { margin-bottom: 11px; }
  .contact__row {
    display: flex;
    align-items: center;
    gap: 9px;
    height: 29px;
  }
  .contact__icon { width: 17px; height: 17px; flex: none; fill: var(--navy); }

  .holder {
    position: absolute;
    right: 58px;
    top: 268px;
    text-align: right;
    font-family: "Source Sans 3", "Helvetica Neue", Arial, sans-serif;
  }
  .holder__name {
    font-size: 27px;
    font-weight: 600;
    color: var(--navy);
    line-height: 32px;
  }
  .holder__role {
    font-size: 20px;
    color: var(--muted);
    line-height: 26px;
  }
  .edge-tab {
    position: absolute;
    right: 0;
    top: 269px;
    width: 15px;
    height: 52px;
    background: var(--navy);
  }

  .card--back .wordmark {
    position: absolute;
    left: 0;
    right: 0;
    top: 150px;
    text-align: center;
    font-size: 118px;
    color: var(--reverse-text);
  }
  .card--back .site {
    position: absolute;
    left: 0;
    right: 0;
    top: 356px;
    text-align: center;
    font-family: "Source Sans 3", "Helvetica Neue", Arial, sans-serif;
    font-size: 20px;
    letter-spacing: 7px;
    color: var(--url-text);
  }
</style>
</head>
<body>
<main class="canvas">
  <section class="card card--front" aria-label="Business card front">
    <div class="wordmark">Cunatel</div>

    <ul class="contact">
      <li class="contact__address">4210 Larchmont Row<br>Fairhaven, Oregon 97512</li>
      <li class="contact__row">
        <svg class="contact__icon" viewBox="0 0 24 24" aria-hidden="true"><path d="M6.6 10.8a15.2 15.2 0 0 0 6.6 6.6l2.2-2.2a1 1 0 0 1 1-.25 11.4 11.4 0 0 0 3.6.57 1 1 0 0 1 1 1V20a1 1 0 0 1-1 1A17 17 0 0 1 3 4a1 1 0 0 1 1-1h3.5a1 1 0 0 1 1 1c0 1.25.2 2.45.57 3.57a1 1 0 0 1-.25 1z"/></svg>
        052-7164291
      </li>
      <li class="contact__row">
        <svg class="contact__icon" viewBox="0 0 24 24" aria-hidden="true"><path d="M2 5h20v14H2z M3.5 6.5 12 13l8.5-6.5" fill="none" stroke="#0b2a63" stroke-width="2"/><path d="M2 5h20L12 12.5z"/></svg>
        tvellingro@cunatel.example
      </li>
      <li class="contact__row">
        <svg class="contact__icon" viewBox="0 0 24 24" aria-hidden="true"><circle cx="12" cy="12" r="10"/><path d="M2 12h20M12 2c3 3 3 17 0 20M12 2c-3 3-3 17 0 20" fill="none" stroke="#ececee" stroke-width="1.4"/></svg>
        www.cunatel.example
      </li>
    </ul>

    <div class="holder">
      <div class="holder__name">Tomas Vellingro</div>
      <div class="holder__role">Attorney</div>
    </div>
    <div class="edge-tab"></div>
  </section>

  <section class="card card--back" aria-label="Business card back">
    <div class="wordmark">Cunatel</div>
    <div class="site">www.cunatel.example</div>
  </section>
</main>
</body>
</html>
```